Improve appearance of one page intro flyer

We modify and upfit medium and heavy duty trucks with equipment needed by the end user. Safety equipment, hydraulic systems, computer systems, etc. We focus on quality and customer service. We have a one page introduction page with wording only. We need graphics or whatever the designer feels would improve the appearance of the flyer and relay professionalism in the presentation.

```html
<!DOCTYPE html>
<html lang="en">
<head>
<meta charset="utf-8">
<title>Ridgeline Custom Trucks — Intro Flyer</title>
<link href="https://fonts.googleapis.com/css2?family=Arimo:wght@700&family=Poppins:ital,wght@0,400;0,500;0,600;0,700;1,600&display=swap" rel="stylesheet">
<style>
  :root{
    --page-bg:#e2e2e2;
    --paper:#ffffff;
    --navy:#2c2a78;
    --header:#46438a;
    --header-deep:#3b3880;
    --ink:#4a4a55;
    --muted-panel:#f1f2f6;
    --white:#ffffff;
  }
  *{margin:0;padding:0;box-sizing:border-box}
  html,body{width:1200px;height:2512px;overflow:hidden;background:var(--page-bg)}
  .flyer{
    position:absolute;left:50px;top:438px;width:784px;height:1165px;
    background:var(--paper);transform:scale(1.403);transform-origin:0 0;
    font-family:"Poppins",sans-serif;color:var(--ink);
    box-shadow:0 6px 18px rgba(0,0,0,.12);
  }
  .hero{position:absolute;left:0;top:0;width:784px;height:378px;overflow:hidden;background:var(--header)}
  .hero-photo{position:absolute;inset:0;
    background:linear-gradient(180deg,#4a478c 0%,#5a5898 45%,#4f4d8f 70%,#3d3a82 100%),
               linear-gradient(90deg,rgba(255,255,255,.06),rgba(180,90,110,.12));
    background-blend-mode:normal}
  .hero-photo::after{content:"";position:absolute;left:0;right:0;top:150px;height:170px;
    background:linear-gradient(90deg,rgba(120,120,170,.35),rgba(110,105,160,.2) 60%,rgba(150,90,120,.25))}
  .brand-mark{position:absolute;left:560px;top:88px;display:flex;align-items:center;gap:8px;
    font-family:"Poppins",sans-serif;font-weight:500;font-size:19px;color:var(--white);line-height:1.15}
  .brand-mark .dot{width:14px;height:14px;border-radius:50%;background:var(--white);flex:none}
  .hero-title{position:absolute;left:76px;top:168px;font-family:"Arimo",sans-serif;font-weight:700;
    font-size:70px;line-height:62px;color:var(--white);letter-spacing:-.5px}
  .hero-tagline{position:absolute;left:80px;top:308px;font-style:italic;font-weight:600;font-size:17.5px;color:var(--white)}
  .section-title{font-family:"Arimo",sans-serif;font-weight:700;color:var(--navy);font-size:22px;line-height:1.05;letter-spacing:.2px}
  .body-copy{font-size:9.6px;line-height:13.3px;text-align:justify}
  .body-copy p+p{margin-top:11px}
  .body-copy b{color:#3a3a48;font-weight:600}
  .overview{position:absolute;left:74px;top:432px;width:298px}
  .mission{position:absolute;left:431px;top:432px;width:278px}
  .overview .section-title,.mission .section-title,.service-area .section-title{margin-bottom:12px}
  .service-area{position:absolute;left:431px;top:572px;width:278px}
  .services-card{position:absolute;left:47px;top:720px;width:346px;height:353px;border:1.5px solid var(--navy);border-radius:12px;padding:24px 0 0 28px}
  .service{position:absolute;left:28px;display:flex;gap:22px}
  .service-photo{width:120px;height:110px;border-radius:8px;border:3px solid #c9c9d3;flex:none}
  .photo-upfit{background:linear-gradient(180deg,#b8bcc6 0%,#9aa2ad 40%,#2f8fb2 65%,#6d6f70 100%)}
  .photo-solutions{background:linear-gradient(180deg,#d8dcdf 0%,#eef0f0 45%,#b8c0a0 70%,#8c8d90 100%)}
  .service-name{font-weight:600;font-size:11.5px;color:#4a4a55;margin:6px 0 6px}
  .service-text{font-size:9.6px;line-height:13px;width:152px;text-align:justify;color:#6a6a75}
  .why-card{position:absolute;left:436px;top:744px;width:281px;height:330px;background:var(--muted-panel);border-radius:12px;padding:24px 28px}
  .why-card .section-title{font-size:21.5px;line-height:26px}
  .why-rule{width:184px;height:2px;background:var(--navy);margin:10px 0 28px}
  .why-card .body-copy{font-size:9.6px}
  .footer{position:absolute;left:0;top:1103px;width:784px;height:62px;background:var(--header-deep);color:var(--white);font-weight:500}
  .footer-contact{position:absolute;left:40px;top:0;height:62px;display:flex;align-items:center;gap:14px;font-size:13px}
  .footer-contact span{display:flex;align-items:center;gap:6px}
  .footer-split{position:absolute;left:440px;top:0}
  .footer-address{position:absolute;left:506px;top:17px;display:flex;gap:16px;align-items:center;font-size:11.5px;line-height:14px}
</style>
</head>
<body>
<main class="flyer">
  <header class="hero">
    <div class="hero-photo" role="img" aria-label="Faded photo of a row of parked semi trucks"></div>
    <div class="brand-mark"><span class="dot"></span><span>Ridgeline<br>Custom Trucks</span></div>
    <h1 class="hero-title">Ridgeline Custom<br>Trucks, Inc.</h1>
    <p class="hero-tagline">Excellence in Custom Truck Modification and Upfitting</p>
  </header>

  <section class="overview">
    <h2 class="section-title">OVERVIEW</h2>
    <div class="body-copy">
      <p>Having <b>more than 30 years</b> in the truck modification industry, Ridgeline Custom Trucks, Inc. specializes in medium- and heavy-duty truck modification and custom-designed upfitting. Based in North Carolina, we transform standard commercial trucks into purpose-built machines designed to meet each customer’s specific needs. From component integration to specialized equipment installations, our specialists provide engineered solutions for all vehicle modifications.</p>
      <p>At <b>Ridgeline Custom Trucks</b> we’re redefining what truck performance and customization can be. Our foundation lies in precision product engineering and quality craftsmanship, ensuring every facet, from upgrades to custom fabrication, is built to last and perform flawlessly. Driven by constant research and development, our team’s design experts are always exploring new technologies, materials, and design improvements to push the limits of what’s possible</p>
    </div>
  </section>

  <section class="mission">
    <h2 class="section-title">MISSION</h2>
    <div class="body-copy">
      <p>Our mission is to redefine quality in truck modification and upfitting by combining craftsmanship, innovation, and reliability.</p>
      <p>At <b>Ridgeline Custom Trucks,</b> our team excels in the highest quality workmanship and reflects the pride and professionalism in everything we do.</p>
    </div>
  </section>

  <section class="service-area">
    <h2 class="section-title">SERVICE AREA</h2>
    <div class="body-copy">
      <p>Serving customers internationally, <b>Ridgeline Custom Trucks, Inc.</b> provides end-to-end solutions for all the major truck manufacturers— from concept and design through final delivery — with nationwide logistics coordination. We are honored to be part of Ironhaul’s Ship Thru service, providing complete upfit service to your new Ironhaul truck — in most cases without any additional shipping charges — delivered directly to your location.</p>
    </div>
  </section>

  <section class="services-card">
    <h2 class="section-title">CORE SERVICES</h2>
    <div class="service" style="top:70px">
      <div class="service-photo photo-upfit" role="img" aria-label="Photo of a blue upfitted flatbed work truck"></div>
      <div>
        <h3 class="service-name">Custom Truck Upfitting</h3>
        <p class="service-text">Tailored designs for vocational and fleet applications - customer-specified safety equipment, computer and camera systems, fenders, decals, tool systems, lighting, hydraulic integration, and much more...</p>
      </div>
    </div>
    <div class="service" style="top:206px">
      <div class="service-photo photo-solutions" role="img" aria-label="Photo of two technicians in safety vests beside a white truck"></div>
      <div>
        <h3 class="service-name" style="margin-top:12px">Specialized Solutions</h3>
        <p class="service-text">Customer interaction to identify and offer specialized solutions to increase efficiency, safety, and reliability.</p>
      </div>
    </div>
  </section>

  <aside class="why-card">
    <h2 class="section-title">WHY CHOOSE<br>RIDGELINE CUSTOM<br>TRUCKS</h2>
    <div class="why-rule"></div>
    <div class="body-copy">
      <p>Our team brings <b>more than 100 years</b> of hands-on expertise in fabrication, mechanical design, and truck engineering.</p>
      <p>Every project reflects our core commitment to Excellence in Every Detail — precision craftsmanship, reliable performance, and tailored functionality that meets each customer’s unique operational goals.</p>
      <p>Our product engineering, design, and quality is what sets us apart as leaders in the truck industry.</p>
    </div>
  </aside>

  <footer class="footer">
    <div class="footer-contact">
      <span>
        <svg width="16" height="16" viewBox="0 0 24 24" fill="none" stroke="#fff" stroke-width="2" stroke-linecap="round" stroke-linejoin="round"><path d="M22 16.9v3a2 2 0 0 1-2.2 2 19.8 19.8 0 0 1-8.6-3.1 19.5 19.5 0 0 1-6-6A19.8 19.8 0 0 1 2.1 4.2 2 2 0 0 1 4.1 2h3a2 2 0 0 1 2 1.7c.1.9.4 1.8.7 2.7a2 2 0 0 1-.5 2.1L8 9.8a16 16 0 0 0 6 6l1.3-1.3a2 2 0 0 1 2.1-.4c.9.3 1.8.6 2.7.7a2 2 0 0 1 1.7 2z"/></svg>
        555-014-0322
      </span>
      <span>
        <svg width="18" height="18" viewBox="0 0 24 24" fill="none" stroke="#fff" stroke-width="2" stroke-linecap="round"><circle cx="12" cy="12" r="4"/><path d="M16 8v5a3 3 0 0 0 6 0v-1a10 10 0 1 0-3.9 7.9"/></svg>
        info@ridgelinecustomtrucks.com
      </span>
    </div>
    <svg class="footer-split" width="60" height="62" viewBox="0 0 60 62"><path d="M0 62 L36 0 L42 0 L6 62 Z" fill="#fff"/></svg>
    <div class="footer-address">
      <svg width="14" height="18" viewBox="0 0 24 30"><path d="M12 0C5.4 0 0 5.3 0 11.8 0 20.6 12 30 12 30s12-9.4 12-18.2C24 5.3 18.6 0 12 0z" fill="#fff"/><circle cx="12" cy="11.5" r="4.2" fill="#3b3880"/></svg>
      <span>482 Commerce Park Drive<br>&nbsp;- Millbrook, NC - 28000</span>
    </div>
  </footer>
</main>
</body>
</html>
```